Rug Cleaning Web Design Project

We need a web design for our cleaning company. We currently have a web page but are not happy with its design. We currently offer fine rug cleaning,upholstery cleaning, and residential and commercial carpet cleanning. We also offer water damage restoration. For our rug cleaning services we offer : Enzyme treatments for pet contamination and odor removal, application of stain protection that is designed for the fine textiles used in rug construction, application of treatments designed to prevent moth damage and pads designed to be used under rugs.Our current web site is harborfreshcare.example. We are intrested in a design with similar information to the web page of Velmora Rug Cleaners INC. We would like to use the colors that are present in our logo that will be uploaded with this description. We would also like this new page to be linked to our other address loomrinsepro.example. We would like the deign to be visually attractive but not "too busy".
Updates

Please include pictures of rugs, or people washing rugs if possible. We do not offer maid type cleaning services. We would not be interested in designs including pictures depicting that type service. Thanks for your hard work on this project.

Dana Whitlow

Industry/Entity Type

Residential

Requirements
Must have
• This page must be viewable on smart phones and tablets.

```html
<!DOCTYPE html>
<html lang="en">
<head>
<meta charset="utf-8">
<meta name="viewport" content="width=1152">
<title>LoomRinsePro – Harbor Fresh Care</title>
<link href="https://fonts.googleapis.com/css2?family=Oswald:wght@400;500&family=Ubuntu:wght@400;500&family=PT+Sans:wght@400;700&display=swap" rel="stylesheet">
<style>
:root{
  --blue:#2f80cc;
  --blue-deep:#1f6cb8;
  --blue-nav:#0b62b3;
  --ink:#2a2a2a;
  --muted:#555;
  --heading-blue:#1a7fc4;
  --footer:#2e2e2e;
  --footer-bar:#4a4a4a;
  --footer-text:#e6e6e6;
}
*{box-sizing:border-box;margin:0;padding:0}
html,body{width:1152px;height:1200px;overflow:hidden}
body{position:relative;background:#fff;font-family:Arial,Helvetica,sans-serif;color:var(--ink)}
.sky{position:absolute;left:0;top:0;width:1152px;height:494px;background:linear-gradient(180deg,#2a7acb 0%,#3b8ad4 60%,#2f7cc6 100%)}
.brand{position:absolute;left:99px;top:0;width:315px;height:123px;background:linear-gradient(#fff,#e4e4e4);border-radius:0 0 26px 26px;box-shadow:0 10px 14px -8px rgba(0,0,0,.35);display:flex;align-items:center;padding-left:18px;gap:12px}
.brand-dot{width:40px;height:40px;border-radius:50%;background:var(--blue-deep)}
.brand-name{font-family:Ubuntu,sans-serif;font-weight:500;font-size:30px;color:#2b2b2b;line-height:1}
.brand-name small{display:block;font-size:11px;letter-spacing:2px;margin-top:4px;text-align:right}
.follow{position:absolute;left:799px;top:20px;display:flex;align-items:center;gap:12px;color:#fff;font-family:Ubuntu,sans-serif;font-weight:500;font-size:18px}
.follow span.c{width:35px;height:35px;border-radius:50%;border:2px solid #fff;background:rgba(255,255,255,.15)}
.nav{position:absolute;left:494px;top:73px;width:561px;height:43px;display:flex;background:linear-gradient(#fff,#e6e6e6);border:1px solid #cfd8e2}
.nav a{display:flex;align-items:center;justify-content:center;font-family:Ubuntu,sans-serif;font-weight:500;font-size:13px;color:#1c3d66;text-decoration:none;border-right:1px solid #d0d0d0;letter-spacing:.3px}
.nav a.on{background:linear-gradient(#1b7bd0,var(--blue-nav));color:#fff}
.promo{position:absolute;left:101px;top:166px;width:273px;height:372px;background:#fff;box-shadow:0 2px 6px rgba(0,0,0,.25);padding:14px 5px}
.tile{height:109px;margin-bottom:15px;background:linear-gradient(90deg,#f1f1f1,#d9d9d9);position:relative;padding:14px 14px}
.tile .art{position:absolute;top:0;bottom:0;width:130px}
.tile p{font-family:Oswald,sans-serif;line-height:1.15;position:relative;white-space:nowrap}
.tile .k{font-size:20px;color:#333}
.tile .t{font-size:25px}
.tile .s{font-family:Arial,sans-serif;font-size:12px;color:#666;margin-top:3px}
.slider{position:absolute;left:397px;top:164px;width:627px;height:372px;background:#fff;padding:4px}
.slider .photo{width:100%;height:100%;background:linear-gradient(135deg,#5a4030 0%,#8a6a52 40%,#c9b39a 60%,#e59a18 85%,#c07010 100%)}
.dots{position:absolute;left:243px;top:296px;width:142px;height:62px;border-radius:31px;background:linear-gradient(#fff,#e2e2e2);display:flex;align-items:center;justify-content:center;gap:14px}
.dots i{width:16px;height:16px;border-radius:50%;background:#6b6b6b}
.dots i.on{background:#1a7fd0}
.shadow{position:absolute;height:14px;border-radius:50%;background:radial-gradient(ellipse,rgba(0,0,0,.3),transparent 70%)}
.cards{position:absolute;left:105px;top:611px;width:920px;height:243px;border:1px dotted #999;display:flex}
.card{flex:1;padding:8px 12px 0;border-right:1px dotted #999;position:relative}
.card:last-child{border-right:0}
.card .pic{height:112px;border:6px solid #f2f2f2;box-shadow:0 0 2px rgba(0,0,0,.3)}
.card h3{font-family:Ubuntu,sans-serif;font-weight:500;font-size:19px;color:#333;margin:10px 0 7px 3px;white-space:nowrap}
.card h3 b{font-weight:500;color:var(--heading-blue)}
.card p{font-size:11.5px;line-height:17px;color:var(--muted);letter-spacing:.3px;text-align:justify;padding:0 3px}
.more{position:absolute;right:14px;bottom:6px;display:flex;align-items:center;gap:5px;font-family:Ubuntu,sans-serif;font-size:12px;color:#444}
.more svg{display:block}
.footer{position:absolute;left:0;top:904px;width:1152px;height:238px;background:var(--footer);color:var(--footer-text)}
.col{position:absolute;top:14px}
.col h4{font-family:"PT Sans",sans-serif;font-weight:400;font-size:21px;color:#fff}
.col h4 b{font-weight:700}
.vr{position:absolute;top:18px;width:2px;height:200px;background:#e8e8e8}
.social li{list-style:none;font-family:"PT Sans",sans-serif;font-weight:700;margin-top:18px;display:flex;align-items:center;gap:8px;color:#cfe0f5;font-size:19px}
.social li i{width:38px;height:38px;background:#3c6bb0;border-radius:4px}
.post p{font-size:11.5px;line-height:23px;letter-spacing:.4px;margin-top:14px}
.arch li{list-style:none;font-size:11.5px;letter-spacing:.5px;line-height:23px}
.arch li::before{content:"";display:inline-block;border:4px solid transparent;border-left-color:#ddd;margin-right:6px}
.arch ul{margin-top:18px}
.field{display:block;margin-top:11px;width:204px;height:28px;border-radius:14px;border:1px solid #bbb;background:#3c3c3c;color:#eee;font-size:11px;padding:6px 10px}
.field.area{height:64px;width:206px;border-radius:12px}
.legal{position:absolute;left:0;top:1142px;width:1152px;height:58px;background:var(--footer-bar);color:#eee;font-size:12px;letter-spacing:.4px;text-align:center;line-height:72px}
</style>
</head>
<body>
<div class="sky"></div>

<header>
  <div class="brand"><span class="brand-dot"></span><div class="brand-name">LoomRinsePro<small>HARBOR FRESH CARE, LLC</small></div></div>
  <div class="follow">Follow Us on <span class="c"></span><span class="c"></span><span class="c"></span></div>
  <nav class="nav">
    <a class="on" style="width:103px" href="#">HOME</a>
    <a style="width:101px" href="#">ABOUT US</a>
    <a style="width:113px" href="#">PORTFOLIO</a>
    <a style="width:126px" href="#">TESTIMONIALS</a>
    <a style="width:118px;border-right:0" href="#">CONTACT US</a>
  </nav>
</header>

<aside class="promo">
  <div class="tile"><div class="art" role="img" aria-label="Hand-knotted oriental rug being washed" style="right:0;background:linear-gradient(90deg,transparent,#c7b6a4 40%,#8a5f44)"></div><p class="k">Fine Rug</p><p class="t" style="color:#2d92b8">Deep Wash</p><p class="s">Learn more</p></div>
  <div class="tile" style="padding-left:136px"><div class="art" role="img" aria-label="Rug fibres treated with enzyme cleaner" style="left:0;background:linear-gradient(90deg,#b0836a,#d3c6bd 80%,transparent)"></div><p class="k">Pet Odor</p><p class="t" style="color:#5a9a2a">Enzyme care</p><p class="s">Learn more</p></div>
  <div class="tile" style="margin-bottom:0"><div class="art" role="img" aria-label="Rolled rugs with protective treatment" style="right:0;background:linear-gradient(90deg,#e2e2e2,#3aaee6 55%,#1a8dd0)"></div><p class="k">Moth &amp; Stain</p><p class="t" style="color:#a8541f">Protection</p><p class="s">Learn more</p></div>
</aside>
<div class="shadow" style="left:110px;top:540px;width:255px"></div>

<section class="slider">
  <div class="photo" role="img" aria-label="Clean oriental rug laid on a polished wood floor in a bright room"></div>
  <div class="dots"><i class="on"></i><i></i><i></i><i></i></div>
</section>
<div class="shadow" style="left:420px;top:538px;width:580px"></div>

<section class="cards">
  <article class="card"><div class="pic" role="img" aria-label="Technician hand washing a wool rug" style="background:linear-gradient(135deg,#e7e2da,#a08870 60%,#4a3a2c)"></div><h3><b>Rug</b> Cleaning</h3><p>Gentle hand washing for fine wool and silk rugs, with careful drying and fringe care for every...</p><a class="more">View More <svg width="22" height="22" viewBox="0 0 22 22"><circle cx="11" cy="11" r="10" fill="#1e7fd0" stroke="#cfe3f5" stroke-width="2"/><path d="M11 6v10M6 11h10" stroke="#fff" stroke-width="3"/></svg></a></article>
  <article class="card"><div class="pic" role="img" aria-label="Upholstered sofa being cleaned" style="background:linear-gradient(135deg,#c98a52,#8a5a36 50%,#e3b08a)"></div><h3><b>Upholstery</b> Care</h3><p>Sofas, chairs and fabric seating refreshed with safe methods that lift soil and keep colours...</p><a class="more">View More <svg width="22" height="22" viewBox="0 0 22 22"><circle cx="11" cy="11" r="10" fill="#1e7fd0" stroke="#cfe3f5" stroke-width="2"/><path d="M11 6v10M6 11h10" stroke="#fff" stroke-width="3"/></svg></a></article>
  <article class="card"><div class="pic" role="img" aria-label="Wall-to-wall carpet in a commercial space" style="background:linear-gradient(180deg,#e4e6e4,#7a7a72 55%,#3a3a34)"></div><h3><b>Carpet</b> Cleaning</h3><p>Residential and commercial carpet cleaning that removes deep dirt, spots and traffic lane...</p><a class="more">View More <svg width="22" height="22" viewBox="0 0 22 22"><circle cx="11" cy="11" r="10" fill="#1e7fd0" stroke="#cfe3f5" stroke-width="2"/><path d="M11 6v10M6 11h10" stroke="#fff" stroke-width="3"/></svg></a></article>
  <article class="card"><div class="pic" role="img" aria-label="Drying equipment on a flooded floor" style="background:linear-gradient(135deg,#d8d2c4,#7f98a8 55%,#3b4f5e)"></div><h3><b>Water</b> Damage</h3><p>Fast water damage restoration with extraction, drying and odor control for homes and...</p><a class="more">View More <svg width="22" height="22" viewBox="0 0 22 22"><circle cx="11" cy="11" r="10" fill="#1e7fd0" stroke="#cfe3f5" stroke-width="2"/><path d="M11 6v10M6 11h10" stroke="#fff" stroke-width="3"/></svg></a></article>
</section>

<footer class="footer">
  <div class="col" style="left:106px"><h4>Social <b>Media</b></h4>
    <ul class="social"><li><i></i>Friendnest</li><li><i></i>Chirpline</li><li><i></i>Workweave</li></ul></div>
  <div class="vr" style="left:302px"></div>
  <div class="col post" style="left:335px;width:230px"><h4 style="margin-left:12px">Recent <b>Post</b></h4>
    <p>How often should a fine wool rug be washed? Our team explains the signs that your rug needs</p>
    <p>Why a quality rug pad protects floors and helps your rug last longer</p></div>
  <div class="vr" style="left:581px"></div>
  <div class="col arch" style="left:612px"><h4><b>Archives</b></h4>
    <ul><li>May 2011</li><li>April 2011</li><li>March 2011</li><li>February 2011</li><li>January 2011</li></ul></div>
  <div class="vr" style="left:777px"></div>
  <div class="col" style="left:802px"><h4>Leave your <b>Message</b></h4>
    <span class="field">----Name----</span>
    <span class="field">----Email----</span>
    <span class="field area">---- Your Message ------</span></div>
</footer>
<div class="legal">Copyright © 2011-12 loomrinsepro.example</div>
</body>
</html>
```